Mutig voran
Wir sind richtig begeistert von dieser Möglichkeit, in kurzer Zeit einen guten Entwurf zu erhalten und auch mitgestalten zu können. Vor allem die Auswahl aus verschiedenen Vorschlägen hat unseren eigenen Blick für das geschärft, was wir wollten. Vielen Dank. Es wird sicher nicht das letzte Mal sein, dass wir diese Möglichkeit nutzen.
Zielgruppe
Zielgruppe sind junge Eltern im Stadtteil Richtsberg in Marburg, einem multikulturellen Stadtteil. Die Stadtteilhebamme begleitet junge Familien am Richtsberg vor und nach der Geburt in den ersten Lebensjahren, die VKM (Nachbarschaftsbund für offene Wege e.V.) ist ein Gemeinwesenprojekt die im Stadtteil Anlaufstelle für Stadtteilbewohner, die Beratungsstellen Wendelhof bestehen aus einer Psychologischen Beratungsstelle mit Erziehungsberatung und einer Schwangerenberatungsstelle (in der Stadt)
Aufgabenstellung
Der Text wird als Datei übermittelt, es soll ein Plakat erstellt werden, das
a) die Kooperation der Beteiligten vermittelt
b) das Angebot nahebringt
c) die Kontaktaufnahme ermöglicht
Das Plakat sollte möglichst auch in verkleinerter Form (Din A5?) gedruckt werden können
Das Logo für die VKM ist als Datei angehängt,
das Logo für die Beratungsstellen ist in drei verschiedenen Dateiformaten angehängt. Hier kann auch der Schriftzug "Solvanta" wegfallen und nur das Ankerstern genutzt werden.

```html
<!DOCTYPE html>
<html lang="de">
<head>
<meta charset="utf-8">
<title>Mutig voran am Richtsberg – Plakat</title>
<link rel="stylesheet" href="https://fonts.googleapis.com/css2?family=Anton&family=Kaushan+Script&family=Fira+Sans+Condensed:wght@500;600&family=Open+Sans:wght@600;700&display=swap">
<style>
  :root {
    --pink: #e0307f;
    --ink: #141414;
    --paper: #f1f1f1;
    --strip: #c9c9c9;
    --backdrop: #8a8a8a;
  }
  * { margin: 0; padding: 0; box-sizing: border-box; }
  html, body { width: 1185px; height: 1200px; overflow: hidden; background: var(--backdrop); }
  .canvas { position: relative; width: 1185px; height: 1200px; }
  .poster {
    position: absolute; left: 167px; top: 0;
    width: 850px; height: 1200px;
    background: var(--paper);
    overflow: hidden;
  }
  .poster__photo {
    position: absolute; left: 575px; top: 0; width: 207px; height: 1200px;
    background: linear-gradient(180deg, #f1f1f1 0%, #d8d8d8 20%, #9a9a9a 38%, #2a2a2a 55%, #1a1a1a 100%);
    -webkit-mask: linear-gradient(90deg, transparent 0%, #000 50%);
            mask: linear-gradient(90deg, transparent 0%, #000 50%);
  }
  .poster__strip { position: absolute; left: 782px; top: 0; width: 68px; height: 1200px; background: var(--strip); }

  .headline { position: absolute; left: 0; top: 0; color: var(--pink); font-weight: 400; }
  .headline__main {
    position: absolute; left: 60px; top: 40px;
    font-family: "Anton", sans-serif; font-size: 175px; line-height: 1; white-space: nowrap;
  }
  .headline__script {
    position: absolute; left: 60px; top: 250px;
    font-family: "Kaushan Script", cursive; font-size: 210px; line-height: 1; white-space: nowrap;
  }
  .headline__place {
    position: absolute; left: 165px; top: 508px;
    font-family: "Anton", sans-serif; font-size: 62px; line-height: 1; white-space: nowrap;
  }

  .offer { position: absolute; left: 52px; top: 618px; width: 520px; color: var(--ink); font-family: "Fira Sans Condensed", sans-serif; }
  .offer__intro { font-weight: 600; font-size: 35px; line-height: 40px; white-space: nowrap; }
  .offer__list { list-style: none; margin-top: 18px; font-weight: 500; font-size: 25px; line-height: 28.6px; white-space: nowrap; }
  .offer__list li { position: relative; padding-left: 16px; }
  .offer__list li::before { content: "•"; position: absolute; left: 0; color: var(--pink); }

  .partners { position: absolute; left: 52px; top: 1062px; font-family: "Open Sans", sans-serif; font-size: 12px; line-height: 16.5px; }
  .partner { position: absolute; top: 0; white-space: nowrap; }
  .partner__name { color: var(--pink); font-weight: 700; }
  .partner__tel { color: var(--ink); font-weight: 600; }
  .partner--midwife { left: 0; top: 25px; }
  .partner--neighbours { left: 162px; }
  .partner--neighbours .partner__mark { position: absolute; left: 0; top: 0; width: 64px; height: 64px; border: 2px solid var(--ink); border-radius: 50%; }
  .partner--neighbours .partner__text { position: absolute; left: 78px; top: 25px; }
  .partner--counsel { left: 440px; }
  .partner--counsel .partner__mark { width: 50px; height: 50px; background: #2a93cf; }
  .partner--counsel .partner__text { margin-top: 14px; }
</style>
</head>
<body>
<div class="canvas">
  <article class="poster">
    <div class="poster__photo" role="img" aria-label="Schwarzweißfoto einer schwangeren Frau im gepunkteten Kleid, die hinter einer Wand hervorschaut"></div>
    <div class="poster__strip"></div>

    <h1 class="headline">
      <span class="headline__main">Mutig</span>
      <span class="headline__script">voran</span>
      <span class="headline__place">am Richtsberg</span>
    </h1>

    <section class="offer">
      <p class="offer__intro">Angebote für Eltern und Kinder<br>in der Schwangerschaft und den<br>ersten Lebensjahren</p>
      <ul class="offer__list">
        <li>Finanzielle Beihilfen</li>
        <li>Beratung in der Schwangerschaft und<br>nach der Geburt</li>
        <li>Hilfe im Antragsdschungel</li>
        <li>Kurse für junge, werdende Mütter</li>
        <li>Leben mit dem Baby</li>
        <li>Wohlfühlprogramme für Eltern und Baby</li>
        <li>Müttererholung- und Genesung</li>
      </ul>
    </section>

    <footer class="partners">
      <div class="partner partner--midwife">
        <div class="partner__name">Stadtteilhebamme</div>
        <div class="partner__tel">Tel.: 0163 5550148</div>
      </div>
      <div class="partner partner--neighbours">
        <div class="partner__mark"></div>
        <div class="partner__text">
          <div class="partner__name">NACHBARSCHAFTSBUND FÜR<br>OFFENE WEGE e.V. (VKM)<br>MARBURG</div>
          <div class="partner__tel">Tel.: 0163 55721</div>
        </div>
      </div>
      <div class="partner partner--counsel">
        <div class="partner__mark"></div>
        <div class="partner__text">
          <div class="partner__name">Wendelhof:</div>
          <div class="partner__tel">Tel.: 0163 55934</div>
        </div>
      </div>
    </footer>
  </article>
</div>
</body>
</html>
```